Unternehmensvorstellung : Broschüre DIN A4 ca. 6 Innenseiten.
Zielgruppe
Dienstleistungen:
- Messdienst und Erstellung Heiz- und Nebenkostenabrechung für Mieter
- Rauchwarnmelder Montage und Wartung
- Trinkwasser/Legionellenprüfung
- Energie-Monitoring-Service (automatisch Ermittlung günstigster Versorger)
Für:
Immobilienverwalter
Immobilienbesitzer
Immobilien Gesellschaften
Architekten und Planer
Aufgabenstellung
siehe Homepage www.wohnarcaplus.de

```html
<!DOCTYPE html>
<html lang="de">
<head>
<meta charset="utf-8">
<title>WohnarcaPlus – Broschüre Umschlag</title>
<link href="https://fonts.googleapis.com/css2?family=Fira+Sans+Condensed:wght@400;500;700&display=swap" rel="stylesheet">
<style>
  :root {
    --brand-blue: #0a8ac9;
    --brand-red: #e0402a;
    --white: #ffffff;
    --headline-box: rgba(20, 45, 85, 0.85);
    --text-dark: #3c4650;
    --photo-top: #6f93c4;
    --photo-bottom: #c9d4df;
  }
  * { margin: 0; padding: 0; box-sizing: border-box; }
  html, body { width: 1200px; height: 424px; overflow: hidden; background: var(--white); }
  body { font-family: "Fira Sans Condensed", Arial, sans-serif; }
  .cover { position: relative; width: 1200px; height: 424px; overflow: hidden; }

  /* back cover */
  .back { position: absolute; left: 0; top: 0; width: 600px; height: 424px; background: var(--brand-blue); }
  .back__band { position: absolute; left: 0; top: 28px; width: 600px; height: 100px; background: var(--white); }
  .back__url { position: absolute; left: 31px; top: 99px; font-size: 13px; font-weight: 700; color: var(--brand-red); }
  .back__contact { position: absolute; left: 31px; top: 300px; color: var(--white); font-size: 7px; line-height: 8.5px; }
  .back__contact p { margin-bottom: 8px; }
  .back__imprint { position: absolute; left: 31px; top: 381px; color: var(--white); font-size: 5px; line-height: 7.5px; font-weight: 500; }

  /* front cover */
  .front { position: absolute; left: 600px; top: 0; width: 600px; height: 424px; }
  .front__art { position: absolute; inset: 0; }
  .front__headline {
    position: absolute; left: 30px; top: 30px; width: 231px; height: 198px;
    background: var(--headline-box); padding: 16px 0 0 14px;
    color: var(--white); font-size: 31px; line-height: 32px; font-weight: 700; letter-spacing: 0.4px;
    text-transform: uppercase; white-space: nowrap;
  }
  .front__brand {
    position: absolute; right: 34px; top: 364px;
    display: flex; align-items: center; gap: 6px;
    font-size: 18px; font-weight: 700; color: var(--text-dark);
  }
  .front__brand-mark { width: 10px; height: 10px; border-radius: 50%; background: var(--text-dark); }
</style>
</head>
<body>
<div class="cover">
  <section class="back">
    <div class="back__band"></div>
    <div class="back__url">wohnarcaplus.de</div>
    <div class="back__contact">
      <p>WohnarcaPlus Deutschland GmbH</p>
      <p>Lindenweg 14<br>63110 Musterau</p>
      <p>+49 (0) 6100 - 12 345 67<br>info@wohnarcaplus.de</p>
    </div>
    <div class="back__imprint">Printed in Germany | Edition 01/2017<br>© Copyright WohnarcaPlus</div>
  </section>

  <section class="front">
    <svg class="front__art" width="600" height="424" viewBox="0 0 600 424">
      <defs>
        <linearGradient id="photoTones" x1="0" y1="0" x2="0" y2="1">
          <stop offset="0" stop-color="var(--photo-top)"/>
          <stop offset="1" stop-color="var(--photo-bottom)"/>
        </linearGradient>
      </defs>
      <polygon role="img" aria-label="Foto: modernes Wohngebäude mit Balkonen und Grünanlage" points="0,0 600,0 600,289 0,358" fill="url(#photoTones)"/>
      <polygon points="0,358 600,289 600,324 0,373" fill="var(--brand-blue)"/>
    </svg>
    <h1 class="front__headline">„Wir bieten<br>mehr als<br>nur den<br>klassischen<br>Messdienst.“</h1>
    <div class="front__brand"><span class="front__brand-mark"></span>WohnarcaPlus Deutschland GmbH</div>
  </section>
</div>
</body>
</html>
```